roofing door hanger

we would like to have our logo kvt roofing, it would be given when we are working in the neighborhood and have our services roof replacement, roof repair, ventilation, inspections. Our slogan is "Reliability starts at the top" . Our company is kvt roofing i would like to get one or two reviews from vorblin, and f any pictures are needed can use pellomart.

Industry/Entity Type

Roofing

Requirements
Must have
• this has to be a door hanger design

```html
<!DOCTYPE html>
<html lang="en">
<head>
<meta charset="utf-8">
<title>KVT Roofing Door Hanger</title>
<link href="https://fonts.googleapis.com/css2?family=Archivo+Black&family=Exo+2:wght@300;500;600&family=Oswald:wght@700&family=Roboto:wght@500;700&display=swap" rel="stylesheet">
<style>
:root{
  --backdrop:#a8a0a1;
  --charcoal:#2a2d30;
  --orange:#f5821f;
  --slate:#585b5e;
  --white:#ffffff;
  --ink:#2a2d30;
}
*{margin:0;padding:0;box-sizing:border-box}
html,body{width:1200px;height:1200px;overflow:hidden;background:var(--backdrop)}
.canvas{position:relative;width:1200px;height:1200px}
.hanger{position:absolute;top:136px;width:458px;height:973px}
.hanger--front{left:110px}
.hanger--back{left:632px}
.hanger-shape{position:absolute;inset:0}
.headline{position:absolute;left:0;width:458px;text-align:center;font-family:"Archivo Black",sans-serif;white-space:nowrap}
.headline__main{top:276px;font-size:51px;color:var(--orange);letter-spacing:.5px;line-height:1}
.headline__sub{top:344px;font-size:32px;color:var(--white);line-height:1}
.offer{position:absolute;top:256px;left:0;width:458px;text-align:center;font-family:"Roboto",sans-serif;font-weight:500;font-size:25.5px;line-height:30px;color:var(--white);white-space:nowrap}
.offer em{font-style:normal;color:var(--orange)}
.brand{position:absolute;left:36px;top:874px;font-family:"Archivo Black",sans-serif;font-size:28px;line-height:30px;color:var(--orange);letter-spacing:1px}
.contact{position:absolute;right:30px;top:860px;width:230px;text-align:right}
.contact__cta{font-family:"Archivo Black",sans-serif;font-size:12.5px;color:var(--orange);letter-spacing:.3px;white-space:nowrap}
.contact__phone{display:flex;justify-content:flex-end;align-items:center;gap:8px;margin-top:2px;font-family:"Oswald",sans-serif;font-weight:700;font-size:29px;color:var(--white);line-height:36px;white-space:nowrap}
.contact__phone svg{width:22px;height:22px}
.contact__rule{height:1px;background:var(--slate);margin:4px 0 6px 30px}
.contact__web{font-family:"Exo 2",sans-serif;font-weight:300;font-size:15.5px;color:var(--orange);white-space:nowrap}
.services{position:absolute;left:28px;top:564px;width:400px;height:262px;border:1.5px solid var(--orange);border-radius:10px}
.services__title{position:absolute;top:-16px;left:50%;transform:translateX(-50%);background:var(--white);padding:0 6px;font-family:"Exo 2",sans-serif;font-weight:600;font-size:24px;color:var(--ink);white-space:nowrap;letter-spacing:.5px}
.service{position:absolute;display:flex;align-items:center;gap:13px;font-family:"Exo 2",sans-serif;font-weight:500;font-size:17px;line-height:20px;color:var(--ink);white-space:nowrap}
.service__icon{width:40px;height:40px;flex:none}
</style>
</head>
<body>
<div class="canvas">

  <section class="hanger hanger--front">
    <svg class="hanger-shape" viewBox="0 0 458 973">
      <rect width="458" height="973" fill="var(--charcoal)"/>
      <polygon points="118,0 170,0 206,64 172,86" fill="var(--backdrop)"/>
      <circle cx="226" cy="144" r="86" fill="var(--backdrop)"/>
      <line x1="0" y1="460" x2="161" y2="416" stroke="var(--slate)" stroke-width="5"/>
      <line x1="293" y1="414" x2="458" y2="460" stroke="var(--slate)" stroke-width="5"/>
      <polygon points="0,470 230,406 458,470 458,488 230,424 0,488" fill="var(--orange)"/>
      <defs>
        <linearGradient id="homeScene" x1="0" y1="0" x2="0" y2="1">
          <stop offset="0" stop-color="#3d8fe0"/>
          <stop offset=".45" stop-color="#b9d4ee"/>
          <stop offset=".65" stop-color="#b8aea2"/>
          <stop offset="1" stop-color="#5f9a3a"/>
        </linearGradient>
      </defs>
      <polygon role="img" aria-label="Photo of a large suburban home with a well-kept roof, lawn and garden under a blue sky" points="0,488 230,424 458,488 458,838 0,838" fill="url(#homeScene)"/>
    </svg>
    <h1 class="headline headline__main">RELIABILITY</h1>
    <p class="headline headline__sub">STARTS AT THE TOP</p>
    <div class="brand">KVT<br>ROOFING</div>
    <div class="contact">
      <div class="contact__cta">CALL FOR A QUOTE TODAY</div>
      <div class="contact__phone">
        <svg viewBox="0 0 24 24"><path d="M6.6 3.5l3 3.2-1.8 2.6c1.2 2.6 3.2 4.6 5.8 5.8l2.6-1.8 3.2 3-1.9 3.2C10.3 19 5 13.7 3.4 6.5z" fill="none" stroke="var(--orange)" stroke-width="2" stroke-linejoin="round"/></svg>
        <span>555-214-0387</span>
      </div>
      <div class="contact__rule"></div>
      <div class="contact__web">WWW.KVT-ROOFING.COM</div>
    </div>
  </section>

  <section class="hanger hanger--back">
    <svg class="hanger-shape" viewBox="0 0 458 973">
      <rect width="458" height="973" fill="var(--charcoal)"/>
      <polygon points="118,0 170,0 206,64 172,86" fill="var(--backdrop)"/>
      <circle cx="226" cy="144" r="86" fill="var(--backdrop)"/>
      <line x1="0" y1="392" x2="161" y2="348" stroke="var(--slate)" stroke-width="5"/>
      <line x1="293" y1="344" x2="458" y2="392" stroke="var(--slate)" stroke-width="5"/>
      <polygon points="0,402 230,336 458,402 458,410 230,350 0,410" fill="var(--orange)"/>
      <defs>
        <linearGradient id="crewScene" x1="0" y1="0" x2="0" y2="1">
          <stop offset="0" stop-color="#4aa3e8"/>
          <stop offset="1" stop-color="#5b5a5c"/>
        </linearGradient>
        <linearGradient id="shingleScene" x1="0" y1="0" x2="1" y2="1">
          <stop offset="0" stop-color="#3b4a80"/>
          <stop offset="1" stop-color="#6e7276"/>
        </linearGradient>
        <linearGradient id="gutterScene" x1="0" y1="0" x2="1" y2="1">
          <stop offset="0" stop-color="#e9e2cc"/>
          <stop offset="1" stop-color="#a79f86"/>
        </linearGradient>
      </defs>
      <polygon role="img" aria-label="Photo of roofers working on a house roof" points="0,410 150,370 150,539 0,539" fill="url(#crewScene)"/>
      <polygon role="img" aria-label="Photo of gloved hands laying roof shingles" points="154,369 230,350 304,369 304,539 154,539" fill="url(#shingleScene)"/>
      <polygon role="img" aria-label="Photo of a white gutter and downspout" points="308,370 458,410 458,539 308,539" fill="url(#gutterScene)"/>
      <rect x="0" y="539" width="458" height="299" fill="var(--white)"/>
    </svg>
    <p class="offer">we offer a <em>15 YEAR</em> warranty with<br>our platinum <em>ROOF PROGRAM</em></p>

    <div class="services">
      <h2 class="services__title">OUR SERVICES</h2>
    </div>
    <div class="service" style="left:38px;top:582px">
      <svg class="service__icon" viewBox="0 0 40 40"><circle cx="20" cy="20" r="20" fill="var(--orange)"/><path d="M9 20l11-8 11 8M12 18v10h16V18" fill="none" stroke="#fff" stroke-width="2"/></svg>
      <span>Roof Installation</span>
    </div>
    <div class="service" style="left:38px;top:631px">
      <svg class="service__icon" viewBox="0 0 40 40"><circle cx="20" cy="20" r="20" fill="var(--orange)"/><path d="M10 14h20v14H10zM10 19h20M10 24h20M15 14v14M20 14v14M25 14v14" fill="none" stroke="#fff" stroke-width="1.6"/></svg>
      <span>Roof Repair</span>
    </div>
    <div class="service" style="left:38px;top:680px">
      <svg class="service__icon" viewBox="0 0 40 40"><circle cx="20" cy="20" r="20" fill="var(--orange)"/><circle cx="20" cy="20" r="2.5" fill="#fff"/><path d="M20 17c-1-5 2-8 5-6s-1 6-5 6zM22.6 21.5c4 3 4 7 1 8s-4-4-1-8zM17.4 21.5c-5 1-8-1-7-4s5-1 7 4z" fill="none" stroke="#fff" stroke-width="1.6"/></svg>
      <span>Attic ventilation</span>
    </div>
    <div class="service" style="left:38px;top:729px">
      <svg class="service__icon" viewBox="0 0 40 40"><circle cx="20" cy="20" r="20" fill="var(--orange)"/><path d="M12 28l12-12M24 12l4 4-3 1-2-2zM12 12l16 16M26 24l2 4-4-2z" fill="none" stroke="#fff" stroke-width="1.8"/></svg>
      <span>Siding Repair</span>
    </div>
    <div class="service" style="left:38px;top:778px">
      <svg class="service__icon" viewBox="0 0 40 40"><circle cx="20" cy="20" r="20" fill="var(--orange)"/><path d="M11 12h7v4h-7zM22 12h7v4h-7zM11 18h7v4h-7zM22 18h7v4h-7zM11 24h7v4h-7zM22 24h7v4h-7z" fill="none" stroke="#fff" stroke-width="1.5"/></svg>
      <span>Gutters</span>
    </div>
    <div class="service" style="left:264px;top:578px">
      <svg class="service__icon" viewBox="0 0 40 40"><circle cx="20" cy="20" r="20" fill="var(--orange)"/><path d="M8 21l12-10 12 10M11 19v10h18V19M17 23h6v6h-6z" fill="none" stroke="#fff" stroke-width="1.8"/></svg>
      <span>Commercial<br>Roofing</span>
    </div>
    <div class="service" style="left:264px;top:656px">
      <svg class="service__icon" viewBox="0 0 40 40"><circle cx="20" cy="20" r="20" fill="var(--orange)"/><path d="M12 12h14v6H12zM18 18v6h-3v6h6v-6h-3M26 15h3" fill="none" stroke="#fff" stroke-width="1.8"/></svg>
      <span>New Siding<br>Installation</span>
    </div>
    <div class="service" style="left:264px;top:726px">
      <svg class="service__icon" viewBox="0 0 40 40"><circle cx="20" cy="20" r="20" fill="var(--orange)"/><circle cx="23" cy="16" r="5" fill="none" stroke="#fff" stroke-width="2"/><path d="M19.5 19.5L11 28" stroke="#fff" stroke-width="2.5" stroke-linecap="round"/></svg>
      <span>Roof<br>Inspection</span>
    </div>

    <div class="brand">KVT<br>ROOFING</div>
    <div class="contact">
      <div class="contact__cta">CALL FOR A QUOTE TODAY</div>
      <div class="contact__phone">
        <svg viewBox="0 0 24 24"><path d="M6.6 3.5l3 3.2-1.8 2.6c1.2 2.6 3.2 4.6 5.8 5.8l2.6-1.8 3.2 3-1.9 3.2C10.3 19 5 13.7 3.4 6.5z" fill="none" stroke="var(--orange)" stroke-width="2" stroke-linejoin="round"/></svg>
        <span>555-214-0387</span>
      </div>
      <div class="contact__rule"></div>
      <div class="contact__web">WWW.KVT-ROOFING.COM</div>
    </div>
  </section>

</div>
</body>
</html>
```